bramblewood mental health web page

this is to be a single page with no links - will function just like an add.
will have 2 biographies
contact info.
Updates

Dear Designers - most of these are too complex.

 Just want one page with contact details (yet to be sorted). No email contact as we can't monitor all emails and if person emails saying suicidal I am potentially accountable if they are successful. Hence- this is just like a listing in a phone book. 
2 photos - one of me the other my husband - with a little blurb next to our names.
No info on fees or appointments etc
I am legally not allowed use language like - "what sets us apart" - it suggests we are better than other clinicians and that is illegal. 
NO EMOTIVE PHOTOS PLEASE! 

Target Market(s)

clients wanting check background and contact information.

Industry/Entity Type

Mental Health

Requirements
Must have
• NEW LOGO
space for photographs
Old web page to complicated
http://wbtk.net.au/index.shtml
Should not have
• anything that flashes.

```html
<!DOCTYPE html>
<html lang="en">
<head>
<meta charset="utf-8">
<title>Bramblewood Mental Health</title>
<link rel="stylesheet" href="https://fonts.googleapis.com/css2?family=Archivo:wght@400;600;700&family=Questrial&display=swap">
<style>
:root{
  --ink:#1c1c1c;
  --muted:#4a4a4a;
  --brand:#1f5563;
  --paper:#ffffff;
  --sea-top:#9fb0ae;
  --sea-bottom:#7f918f;
  --cliff-light:#e4e0d6;
  --cliff-dark:#b7b1a3;
  --water-top:#8ea19f;
  --water-bottom:#6e807e;
}
*{margin:0;padding:0;box-sizing:border-box}
html,body{width:1200px;height:2664px;overflow:hidden;background:var(--paper)}
body{position:relative;font-family:"Archivo",Arial,sans-serif;color:var(--ink)}
.abs{position:absolute}

.brand{left:128px;top:56px;display:flex;align-items:center;gap:18px}
.brand-square{width:84px;height:84px;background:var(--brand)}
.brand-name{font-family:"Archivo",Arial,sans-serif;font-weight:700;font-size:38px;line-height:1.05;color:var(--brand);text-transform:uppercase;letter-spacing:1px}

.header-contact{left:772px;top:92px;font-size:14px;line-height:26px;color:var(--ink)}

.hero{left:0;top:222px;width:1200px;height:250px;background:linear-gradient(180deg,var(--sea-top),var(--sea-bottom))}

.practitioner{left:128px;top:520px}
.practitioner-name{font-weight:700;font-size:22px}
.practitioner-name em{font-weight:600;font-size:16px;font-style:italic}
.practitioner-reg{margin-top:8px;font-size:12px;color:var(--muted)}

.col-heading{font-family:"Questrial",Arial,sans-serif;font-size:23px;line-height:44px;text-transform:uppercase;letter-spacing:.5px}
.item-list{list-style:none;font-size:13.5px;line-height:26px;margin-top:28px;color:var(--ink)}

.treats{left:128px;top:734px;width:270px}
.assess{left:128px;top:1150px;width:280px}
.services{left:456px;top:734px;width:250px}
.other{left:456px;top:1360px;width:250px}

.photo{background:linear-gradient(180deg,var(--cliff-light),var(--cliff-dark))}
.photo-one{left:772px;top:742px;width:298px;height:448px}
.photo-two{left:772px;top:1654px;width:298px;height:480px;background:linear-gradient(180deg,var(--water-top),var(--water-bottom))}

.bio-title{font-weight:700;font-size:26px}
.bio-sub{font-weight:700;font-style:italic;font-size:16px;margin-top:4px}
.bio-text{margin-top:30px;font-size:12.5px;line-height:26px;color:var(--muted);width:300px}
.bio-one{left:772px;top:1236px}
.bio-two{left:772px;top:2152px}

.contact-label{font-family:"Questrial",Arial,sans-serif;font-size:36px;letter-spacing:1px;text-transform:uppercase}
.contact-value{font-style:italic;font-size:22px;margin-top:14px;color:var(--ink)}
.phone{left:128px;top:2046px}
.address{left:128px;top:2224px}
</style>
</head>
<body>

<header>
  <div class="abs brand">
    <span class="brand-square"></span>
    <span class="brand-name">Bramblewood<br>Mental Health</span>
  </div>
  <div class="abs header-contact">
    <p>Phone: (08) 9000 4182 or 0400 316 275</p>
    <p>Address: 24 Larkspur Way, ALDERTON 6021</p>
  </div>
</header>

<div class="abs hero" role="img" aria-label="Calm coastal photograph of pale cliffs above the sea"></div>

<section class="abs practitioner">
  <p class="practitioner-name">Maren Holt <em>M. Psych (Clinical), M. Genetic Couns., B.A. (Psych),</em></p>
  <p class="practitioner-reg">Reg. no. PSY0000112233 Provider no. 5512093L Member of the Allied Psychology Guild</p>
</section>

<section class="abs treats">
  <h2 class="col-heading">Specialising in the treatment of:</h2>
  <ul class="item-list">
    <li>Depression</li>
    <li>Anxiety</li>
  </ul>
</section>

<section class="abs assess">
  <h2 class="col-heading">Provider of psychological assessment and therapy for other mental health problems including:</h2>
  <ul class="item-list">
    <li>Phobias</li>
    <li>Panic</li>
    <li>Adjustment disorder</li>
    <li>Bereavement</li>
    <li>Post traumatic stress</li>
    <li>disorder</li>
    <li>Eating disorders</li>
    <li>Obsessive</li>
    <li>Compulsive disorder</li>
    <li>Bipolar disorder</li>
    <li>Vocal dysphonia</li>
    <li>Sleep problems</li>
    <li>Post natal issues</li>
  </ul>
</section>

<section class="abs services">
  <h2 class="col-heading">Counselling and therapy provided for:</h2>
  <ul class="item-list">
    <li>Families</li>
    <li>Couples (Couple Care &amp;</li>
    <li>Relate Program)</li>
    <li>Group</li>
    <li>Individuals</li>
    <li>Children</li>
    <li>Adolescents</li>
    <li>Adults</li>
    <li>Older persons</li>
  </ul>
</section>

<section class="abs other">
  <h2 class="col-heading">Other services:</h2>
  <ul class="item-list">
    <li>Cognitive Assessment</li>
    <li>Neuropsychological</li>
    <li>Assessment</li>
    <li>Memory &amp; Dementia</li>
    <li>Screening</li>
    <li>Employee Assistance</li>
    <li>Program</li>
    <li>Stress Management</li>
    <li>Medicolegal reports</li>
  </ul>
</section>

<div class="abs photo photo-one" role="img" aria-label="Portrait photograph space for the first practitioner"></div>

<section class="abs bio-one">
  <h3 class="bio-title">Lorem ipsum</h3>
  <p class="bio-sub">dolor sit amet, elit.</p>
  <p class="bio-text">dolor sit amet, consectetur adipiscing elit. Duis tincidunt nibh eu magna dictum at bibendum nulla faucibus varius eget. Curabitur lobortis risus ut urna imperdiet commodo. Nulla facilisi. Nullam ac felis metus, non ultrices nisl.</p>
</section>

<div class="abs photo photo-two" role="img" aria-label="Portrait photograph space for the second practitioner"></div>

<section class="abs bio-two">
  <h3 class="bio-title">Lorem ipsum</h3>
  <p class="bio-sub">dolor sit amet, elit.</p>
  <p class="bio-text">dolor sit amet, consectetur adipiscing elit. Duis tincidunt nibh eu magna dictum at bibendum nulla faucibus varius eget. Curabitur lobortis risus ut urna imperdiet commodo. Nulla facilisi. Nullam ac felis metus, non ultrices nisl.</p>
</section>

<section class="abs phone">
  <h2 class="contact-label">Phone:</h2>
  <p class="contact-value">(08) 9000 4182 or 0400316275</p>
</section>

<section class="abs address">
  <h2 class="contact-label">Address:</h2>
  <p class="contact-value">24 Larkspur Way, ALDERTON 6021</p>
</section>

</body>
</html>
```